Lantern Pact, Steady Path. (Website Design)

We are launching a new bipartisan civic movement: Lantern Pact. Steady Path.
The mission is this: Americans deserve a government that is legally required to serve them honestly.
We are looking for a world-class website designer capable of creating an emotionally powerful, modern, cinematic landing page experience that feels larger than politics.
This is not a campaign website for a political party or candidate. We are not looking for a red, white, and blue page with stripes, or American flags, or stock footage of smiling people in a voting booth. We are looking for an emotional and cinematic experience through and through.
The visual direction should feel:
Historic
Hopeful
American
Emotional
Cinematic
Trustworthy
Timeless
The goal is to make visitors feel that they are witnessing the beginning of something important and want to be part of it in the end.
Primary Objective:
Inspire visitors to participate in a one-minute survey and cast their vote.
The survey itself is extremely short and takes approximately one minute to complete.
Everything on the page should ultimately guide visitors toward this action while creating enough curiosity, trust, emotional engagement, and excitement that they feel compelled to take part in the movement.
Audience:
The audience is ordinary Americans across the political spectrum: Democrats, Republicans, Independents.
The design should feel unifying and welcoming.
It should avoid looking partisan, ideological, activist, or government-issued.
Creative Freedom:
We are intentionally giving designers substantial creative freedom.
We are not looking for someone to simply arrange content into predefined sections.
Instead, we are looking for a designer who can think strategically about user experience and persuasion.
The ideal design is as minimal as possible, but you may always:
Use as many sections as you believe are necessary.
Use as many images as you believe are necessary.
Include storytelling elements.
Include data visualizations.
Include timelines.
Include videos.
Include animations.
Include or exclude sections as you see fit.
Reorganize the flow entirely.
We uploaded some files containing text and section suggestions. You don’t have to use them.
We also uploaded some images to convey the general feel we’re looking for.
We are much more interested in the effectiveness of the overall experience than in any specific layout.
What success looks like:
Think outside the box.
Please do not create another generic political website. We have already explored those approaches.
We are looking for something different.
The winning design will be the one that most effectively guides visitors from curiosity to belief to participation.
When a visitor reaches the end of the experience, they should feel:
This is bigger than politics.
This is something I can support regardless of party.
This feels credible.
This feels hopeful.
I want to be part of this.
Use the survey results, the research findings, the principles, the storytelling, or any other elements you believe will help build trust and inspire participation.
Don't just impress us with flashy visuals. Impress us with a website experience that inspires people to become part of the movement and cast their vote.
The final call-to-action should feel like the natural conclusion of the journey, not a request for engagement.
Our goal is not simply to inform visitors. Our goal is to inspire them to cast their vote.
Prioritize emotional impact, storytelling, clarity, and persuasion over decorative design elements.
Final words:
Design a website experience that successfully inspires visitors to take the survey and cast their vote.
Think like a storyteller, not just a designer.
Thank you for your interest in the project.
Best of luck.

```html
<!DOCTYPE html>
<html lang="en">
<head>
<meta charset="utf-8">
<title>Lantern Pact. Steady Path.</title>
<link href="https://fonts.googleapis.com/css2?family=Libre+Baskerville:wght@400;700&family=Inter:wght@400;500;600;700&display=swap" rel="stylesheet">
<style>
:root{
  --backdrop:#b9b9bb;
  --ink:#0c0b0a;
  --ink-2:#141311;
  --card:#1a1917;
  --line:#2e2b27;
  --gold:#e8c47e;
  --gold-deep:#c99a4b;
  --cream:#f4ecdc;
  --muted:#a39b8e;
  --soft:#cfc7b8;
  --strip:#d9d9dd;
}
*{margin:0;padding:0;box-sizing:border-box}
html,body{width:1200px;height:3987px;overflow:hidden;background:var(--backdrop)}
body{font-family:"Inter",sans-serif;color:var(--cream)}
.page{position:absolute;left:90px;top:90px;width:1020px;height:3808px;background:var(--ink);overflow:hidden;box-shadow:0 10px 40px rgba(0,0,0,.25)}
section,footer{position:relative;width:100%}
.abs{position:absolute}
.serif{font-family:"Libre Baskerville",serif;letter-spacing:-.03em}
.eyebrow{font-size:8px;font-weight:700;letter-spacing:.14em;text-transform:uppercase;color:var(--gold)}
.btn-gold{display:inline-flex;align-items:center;justify-content:center;background:linear-gradient(180deg,#f1d597,var(--gold-deep));color:#1a1207;font-weight:700;border-radius:999px}
.btn-line{display:inline-flex;align-items:center;justify-content:center;border:1px solid #5a5145;color:var(--cream);font-weight:700;border-radius:999px;background:rgba(0,0,0,.3)}

/* hero */
.hero{height:621px;background:linear-gradient(180deg,#1e1c19 0%,#171512 70%,#0f0e0c 100%)}
.hero-photo{position:absolute;inset:0;background:
  radial-gradient(ellipse 220px 300px at 170px 330px,rgba(120,92,62,.55),transparent 70%),
  radial-gradient(ellipse 200px 260px at 880px 300px,rgba(150,120,92,.45),transparent 70%),
  radial-gradient(ellipse 120px 90px at 510px 130px,rgba(110,90,80,.5),transparent 70%),
  linear-gradient(180deg,#2a2722,#1a1815 60%,#12100e)}
.brand{left:18px;top:20px;display:flex;align-items:center;gap:10px}
.brand-mark{width:74px;height:74px;border-radius:50%;border:2px solid var(--gold-deep);background:#15120e}
.brand-name{font-family:"Libre Baskerville",serif;font-size:21px;line-height:1.1;color:var(--gold);letter-spacing:-.02em}
.nav{right:18px;top:18px;display:flex;align-items:center;gap:28px;font-size:10.5px;font-weight:500}
.nav .vote{border:1px solid var(--cream);border-radius:999px;padding:5px 10px}
.hero .eyebrow{left:240px;top:155px;color:var(--cream)}
.hero-title{left:238px;top:170px;font-size:80px;line-height:74px;color:var(--cream);font-weight:700}
.hero-lede{left:240px;top:416px;font-size:18px;line-height:26px;width:440px;color:var(--soft)}
.hero-ctas{left:240px;top:486px;display:flex;gap:10px}
.hero-ctas .btn-gold,.hero-ctas .btn-line{height:31px;padding:0 16px;font-size:10px}
.scroll{left:0;width:100%;top:590px;text-align:center;font-size:7px;letter-spacing:.2em;color:var(--muted)}

/* mission */
.mission{height:1040px;background:linear-gradient(180deg,#0d0c0b,#0a0909)}
.mission .eyebrow{left:235px;top:74px}
.mission-title{left:234px;top:90px;width:560px;font-size:46px;line-height:45px;color:var(--cream)}
.mission-copy{left:235px;top:288px;font-size:10px;color:var(--soft);line-height:31px}
.agree-box{left:235px;top:357px;width:546px;height:65px;border:1px solid var(--line);border-radius:12px;background:var(--ink-2);display:flex;align-items:center;justify-content:space-between;padding:0 18px}
.agree-box span{font-family:"Libre Baskerville",serif;font-size:17px}
.agree-box .btn-gold{height:27px;padding:0 14px;font-size:9px}
.about-eyebrow{left:163px;top:560px}
.about-title{left:162px;top:576px;font-size:46px;line-height:45px;color:var(--cream)}
.about-copy{left:163px;top:676px;width:500px;font-size:10px;line-height:19px;color:var(--soft)}
.timeline{left:163px;top:741px;width:693px;display:grid;grid-template-columns:repeat(4,1fr);gap:12px}
.step{height:184px;border:1px solid var(--line);border-radius:10px;background:var(--ink-2);padding:18px 16px}
.step .date{display:inline-block;background:#f1ead8;color:#111;font-size:7px;font-weight:700;border-radius:999px;padding:3px 8px}
.step h3{font-family:"Libre Baskerville",serif;font-size:15px;line-height:17px;margin:14px 0 14px;font-weight:400}
.step p{font-size:9px;line-height:15px;color:var(--muted)}
.results-line{left:0;width:100%;top:956px;text-align:center;font-family:"Libre Baskerville",serif;font-size:19px;color:var(--cream)}

/* agrees */
.agrees{height:398px;background:radial-gradient(ellipse 420px 240px at 50% 40%,#2b251c,#0b0a09 75%)}
.agrees .eyebrow{left:0;width:100%;top:94px;text-align:center;font-size:7px}
.agrees-title{left:0;width:100%;top:128px;text-align:center;font-size:46px;line-height:44px}
.agrees-copy{left:0;width:100%;top:222px;text-align:center;font-size:10px;line-height:19px;color:var(--soft)}
.agrees .btn-gold{left:375px;top:276px;height:33px;width:135px;font-size:10px}
.counter{text-align:center}
.counter b{display:block;font-family:"Libre Baskerville",serif;font-weight:400;font-size:26px;color:var(--cream);letter-spacing:-.02em}
.counter small{font-size:6.5px;letter-spacing:.12em;color:var(--muted);text-transform:uppercase}
.agrees .counter{left:524px;top:270px}

/* strip */
.strip{height:200px;background:var(--strip)}
.strip-photo{position:absolute;top:24px;height:148px}

/* survey */
.survey{height:592px;background:#0c0b0a}
.survey-card{left:163px;top:61px;width:693px;height:469px;border:1px solid var(--line);border-radius:14px;background:linear-gradient(180deg,#1b1a18,#121110);padding:0 29px}
.survey-card .eyebrow{position:absolute;left:29px;top:48px;color:var(--soft);font-size:10px;letter-spacing:.2em}
.survey-title{left:29px;top:66px;width:600px;font-size:46px;line-height:44px}
.survey-copy{left:29px;top:176px;width:620px;font-size:10px;line-height:19px;color:var(--soft)}
.stats{left:29px;top:232px;width:635px;display:grid;grid-template-columns:repeat(3,1fr);gap:10px}
.stat{height:97px;border:1px solid var(--line);border-radius:8px;background:#0f0e0d;padding:14px 14px}
.stat b{display:block;font-family:"Libre Baskerville",serif;font-weight:400;font-size:52px;line-height:60px;color:#f7e2b3;letter-spacing:-.03em}
.stat small{font-size:6.5px;letter-spacing:.12em;color:var(--muted)}
.bars{left:29px;top:354px;width:626px}
.bar-row{display:flex;align-items:center;height:20px;font-size:8px;color:var(--soft)}
.bar-row .label{width:77px}
.bar-row .track{flex:1;height:6px}
.bar-row .fill{height:6px;border-radius:3px;background:linear-gradient(90deg,#c99a4b,#f3d9a0)}
.bar-row .pct{width:40px;text-align:right;font-size:7.5px}
.survey-card .btn-line{position:absolute;left:29px;top:426px;height:24px;padding:0 12px;font-size:7px;letter-spacing:.1em}

/* principles */
.principles{height:341px;background:linear-gradient(180deg,#0e0d0c,#090808)}
.principles .eyebrow{left:0;width:100%;top:72px;text-align:center;font-size:7px}
.principles-title{left:0;width:100%;top:106px;text-align:center;font-size:46px;line-height:44px}
.principles-copy{left:0;width:100%;top:194px;text-align:center;font-size:10px;color:var(--soft)}
.principles .btn-line{left:448px;top:228px;height:24px;width:122px;font-size:7px;letter-spacing:.1em}

/* final vote */
.finale{height:554px;background:radial-gradient(ellipse 420px 260px at 50% 40%,#2c261d,#0a0908 75%)}
.finale .eyebrow{left:0;width:100%;top:136px;text-align:center;font-size:11px;letter-spacing:.22em;color:var(--soft)}
.finale-title{left:0;width:100%;top:170px;text-align:center;font-size:46px;line-height:46px}
.finale-copy{left:225px;width:570px;top:266px;text-align:center;font-size:10.5px;line-height:19px;color:var(--soft)}
.finale .btn-gold{left:420px;top:335px;height:33px;width:176px;font-size:10.5px}
.finale .counter{left:0;width:100%;top:382px}
.finale .counter b{font-size:34px}
.footer{height:62px;background:#0b0a09;border-top:1px solid #1c1a17;font-size:8px;color:var(--muted)}
.footer .copy{left:163px;top:34px}
.footer .top{right:163px;top:22px}
</style>
</head>
<body>
<div class="page">

  <section class="hero">
    <div class="hero-photo" role="img" aria-label="Sepia cinematic photo collage: a historic statesman on the left, a smiling young girl on the right, a waving flag and a crowd in the haze"></div>
    <div class="abs brand">
      <span class="brand-mark"></span>
      <span class="brand-name">Lantern Pact.<br>Steady Path.</span>
    </div>
    <nav class="abs nav">
      <span>HOME</span><span>MISSION</span><span>PRINCIPLES</span><span>RESULTS</span><span class="vote">VOTE NOW</span>
    </nav>
    <p class="abs eyebrow">A bipartisan civic movement</p>
    <h1 class="abs hero-title serif">Lantern<br>Pact. Steady<br>Path.</h1>
    <p class="abs hero-lede">Americans deserve a government that is legally required to serve them honestly.</p>
    <div class="abs hero-ctas"><span class="btn-gold">Cast Your Vote</span><span class="btn-line">Watch the Story</span></div>
    <p class="abs scroll">SCROLL</p>
  </section>

  <section class="mission">
    <p class="abs eyebrow">Mission statement</p>
    <h2 class="abs mission-title serif">Today, not a single law binds our government to act honestly, and in our best interest.</h2>
    <p class="abs mission-copy">If our government exists solely to serve us, why isn't it legally required to?<br>We founded this movement to change that.</p>
    <div class="abs agree-box"><span>Do you agree?</span><span class="btn-gold">Vote Now</span></div>

    <p class="abs eyebrow about-eyebrow">Who we are</p>
    <h2 class="abs about-title serif">From a simple idea to a<br>national framework.</h2>
    <p class="abs about-copy">A bipartisan movement based in Washington, D.C., built around one simple idea: government should faithfully serve the people, not special interests.</p>
    <div class="abs timeline">
      <article class="step"><span class="date">August 2024</span><h3>The nonprofit began</h3><p>We started a nonprofit with one goal in mind: Americans deserve an honest government.</p></article>
      <article class="step"><span class="date">October 2025</span><h3>The principles emerged</h3><p>We identified 10 principles that most Americans agree our government must uphold.</p></article>
      <article class="step"><span class="date">March 2026</span><h3>The framework formed</h3><p>We turned those principles into a rigorous framework and named it Lantern Pact.</p></article>
      <article class="step"><span class="date">April 2026</span><h3>The study was tested</h3><p>We tested the framework in a pre-registered national study with Americans across the political spectrum.</p></article>
    </div>
    <p class="abs results-line">And the results exceeded all our expectations.</p>
  </section>

  <section class="agrees">
    <p class="abs eyebrow">Your voice matters</p>
    <h2 class="abs agrees-title serif">America agrees more<br>than we think.</h2>
    <p class="abs agrees-copy">Across political lines, Americans are saying yes to a government legally required to<br>serve the people honestly. Add your voice in one minute.</p>
    <span class="abs btn-gold">Cast Your Vote</span>
    <div class="abs counter"><b>1,016</b><small>People already voted yes</small></div>
  </section>

  <section class="strip">
    <div class="strip-photo" style="left:0;width:428px;background:linear-gradient(90deg,#8a7460,#c9b49a 40%,#9a8670 70%,#d8cbb6)" role="img" aria-label="Sepia archival photographs of early suffrage marchers with a starred banner"></div>
    <div class="strip-photo" style="left:447px;width:484px;background:linear-gradient(90deg,#3a2e24,#a3805a 40%,#6b5440 65%,#b4a590)" role="img" aria-label="Archival portraits of civil rights leaders in black and white and warm tones"></div>
    <div class="strip-photo" style="left:950px;width:70px;background:linear-gradient(90deg,#7d6a58,#b9a992)" role="img" aria-label="Archival photograph of a crowd before a domed capitol"></div>
  </section>

  <section class="survey">
    <div class="abs survey-card">
      <p class="eyebrow">The survey</p>
      <h2 class="abs survey-title serif">Support held across party lines.</h2>
      <p class="abs survey-copy">We laid out the principles, then asked Americans if they would support a legal framework built around them. Most reforms lose support once the details appear. This one didn't.</p>
      <div class="abs stats">
        <div class="stat"><b>82.9</b><small>% SAID YES</small></div>
        <div class="stat"><b>89.9</b><small>% AGREE</small></div>
        <div class="stat"><b>2.7</b><small>% OPPOSED</small></div>
      </div>
      <div class="abs bars">
        <div class="bar-row"><span class="label">Democrats</span><div class="track"><div class="fill" style="width:88%"></div></div><span class="pct">84.5%</span></div>
        <div class="bar-row"><span class="label">Republicans</span><div class="track"><div class="fill" style="width:83%"></div></div><span class="pct">80.2%</span></div>
        <div class="bar-row"><span class="label">Independents</span><div class="track"><div class="fill" style="width:83%"></div></div><span class="pct">79.9%</span></div>
      </div>
      <span class="btn-line">READ THE DETAILS OF THE STUDY</span>
    </div>
  </section>

  <section class="principles">
    <p class="abs eyebrow">The seven principles</p>
    <h2 class="abs principles-title serif">What honest public<br>service should require.</h2>
    <p class="abs principles-copy">89.9% of Americans said they agree.</p>
    <span class="abs btn-line">READ THE PRINCIPLES</span>
  </section>

  <section class="finale">
    <p class="abs eyebrow">One minute. One voice.</p>
    <h2 class="abs finale-title serif">Be part of history. Vote<br>now.</h2>
    <p class="abs finale-copy">For decades, we have argued over policies, parties, and ideologies. But today, across political lines, generations, and races, Americans are arriving at the same conclusion: we deserve a government legally required to serve the people honestly.</p>
    <span class="abs btn-gold">Take the 1-Minute Survey</span>
    <div class="abs counter"><b>1,016</b><small>People already voted yes for the ballot</small></div>
  </section>

  <footer class="footer">
    <span class="abs copy">© 2026 Lantern Pact. Steady Path.</span>
    <span class="abs top">Back to top</span>
  </footer>
</div>
</body>
</html>
```